Mindfulness School for Children -- Business Cards

We're looking for business cards for our school directors and owners. We're a mindfulness school for children called little compass. Attached are our logos/icons.

```html
<!DOCTYPE html>
<html lang="en">
<head>
<meta charset="utf-8">
<title>little compass — Business Cards</title>
<link rel="stylesheet" href="https://fonts.googleapis.com/css2?family=Montserrat:wght@400;500&display=swap">
<style>
  :root {
    --page: #dcdcdc;
    --card: #efefef;
    --teal: #3f9db0;
    --teal-deep: #3a93a8;
    --green: #8fc89b;
    --green-soft: #9dcd93;
    --ink: #333638;
    --white: #ffffff;
  }
  * { margin: 0; padding: 0; box-sizing: border-box; }
  html, body {
    width: 1200px; height: 1164px; overflow: hidden;
    background: var(--page);
    font-family: "Montserrat", sans-serif;
  }
  .sheet {
    width: 1200px; height: 1164px;
    display: flex; align-items: center; justify-content: center; gap: 40px;
  }
  .card {
    position: relative;
    width: 540px; height: 306px;
    overflow: hidden;
    box-shadow: 0 2px 6px rgba(0,0,0,.18);
  }

  /* Front */
  .card-front { background: var(--card); }
  .brand-name {
    position: absolute; left: 46px; top: 38px;
    font-size: 30px; font-weight: 500; letter-spacing: .2px;
    color: var(--teal);
  }
  .holder {
    position: absolute; right: 35px; top: 106px; text-align: right;
  }
  .holder-name {
    font-size: 18px; font-weight: 500; color: var(--teal); letter-spacing: .3px;
  }
  .holder-role {
    margin-top: 4px; font-size: 12px; color: var(--green);
  }
  .contact {
    position: absolute; left: 44px; top: 159px;
    list-style: none; font-size: 12.5px; color: var(--ink); line-height: 1.35;
  }
  .contact li { display: flex; align-items: flex-start; gap: 7px; margin-bottom: 4px; }
  .contact li:first-child { margin-bottom: 7px; }
  .contact svg { width: 10px; height: 11px; flex: none; margin-top: 2px; fill: var(--green); }
  .wave { position: absolute; left: 0; bottom: 0; width: 540px; height: 70px; }
  .website {
    position: absolute; right: 37px; bottom: 8px;
    font-size: 11px; color: var(--white); letter-spacing: .2px;
  }

  /* Back */
  .card-back {
    background: linear-gradient(125deg, var(--teal) 0%, #6fb5ae 40%, var(--green) 75%, var(--green-soft) 100%);
  }
  .back-art {
    position: absolute; left: 0; top: 20px; width: 310px; height: 286px;
    background: radial-gradient(ellipse at 40% 60%, rgba(160,210,150,.55) 0%, rgba(80,165,185,.35) 55%, rgba(80,165,185,0) 80%);
  }
  .back-brand {
    position: absolute; left: 155px; top: 138px; width: 260px; text-align: center;
    font-size: 30px; font-weight: 500; color: var(--white);
  }
</style>
</head>
<body>
<main class="sheet">
  <section class="card card-front" aria-label="Business card front">
    <div class="brand-name">little compass</div>

    <div class="holder">
      <div class="holder-name">DANIEL REYES</div>
      <div class="holder-role">Founder / CEO</div>
    </div>

    <ul class="contact">
      <li>
        <svg viewBox="0 0 10 12"><path d="M5 0a4 4 0 0 0-4 4c0 3 4 8 4 8s4-5 4-8a4 4 0 0 0-4-4zm0 5.6A1.6 1.6 0 1 1 5 2.4a1.6 1.6 0 0 1 0 3.2z"/></svg>
        <span>Your Office Address<br>City Country AB 3434</span>
      </li>
      <li>
        <svg viewBox="0 0 12 12"><path d="M2.5 1 4.5 3 3.6 4.6a6.5 6.5 0 0 0 3.8 3.8L9 7.5l2 2-1.3 1.5C5.5 11 1 6.5 1 2.3z"/></svg>
        <span>555 0148 260</span>
      </li>
      <li>
        <svg viewBox="0 0 10 12"><path d="M2 0h6a1 1 0 0 1 1 1v10a1 1 0 0 1-1 1H2a1 1 0 0 1-1-1V1a1 1 0 0 1 1-1zm.5 1.5v8h5v-8zM5 10.2a.6.6 0 1 0 0 .01z"/></svg>
        <span>555 0148 260</span>
      </li>
      <li>
        <svg viewBox="0 0 12 10"><path d="M0 1h12v8H0zm1.2 1 4.8 3.3L10.8 2z"/></svg>
        <span>info@littlecompass.com</span>
      </li>
    </ul>

    <svg class="wave" viewBox="0 0 540 70" preserveAspectRatio="none" aria-hidden="true">
      <path d="M0 8 C90 40 210 58 330 44 C430 33 490 34 540 38 L540 70 L0 70Z" fill="var(--green)"/>
      <path d="M0 18 C95 48 215 64 335 52 C435 43 490 42 540 44 L540 70 L0 70Z" fill="var(--teal-deep)"/>
    </svg>
    <div class="website">www.littlecompass.com</div>
  </section>

  <section class="card card-back" aria-label="Business card back">
    <div class="back-art" role="img" aria-label="Large soft brand emblem decoration in teal and green tones"></div>
    <div class="back-brand">little compass</div>
  </section>
</main>
</body>
</html>
```